K&R Security Services PTY. LTD.

Ive just had my logo made and I'm looking for some simple but strong designs for my business cards the company is a security company.

Please use dark colors.

Regards,

Owen Deloit

Reason: Need more time for discussion with other directors

Industry/Entity Type

Security

Font styles to use
Sans Serif
Decorative

```html
<!DOCTYPE html>
<html lang="en">
<head>
<meta charset="utf-8">
<title>K&amp;R Security Services – Business Card</title>
<link rel="stylesheet" href="https://fonts.googleapis.com/css2?family=Open+Sans:wght@400;600&family=Libre+Baskerville:wght@400&display=swap">
<style>
  :root {
    --stage: #141414;
    --card-black: #1b1b1b;
    --card-white: #f7f7f7;
    --ink: #2a2a2a;
    --ink-soft: #6d6d6d;
    --rule: #9a9a9a;
    --band-grey: #a9a9a9;
    --band-black: #1c1c1c;
    --mark-light: #e6e6e6;
  }
  * { box-sizing: border-box; margin: 0; padding: 0; }
  html, body {
    width: 1200px; height: 900px; overflow: hidden;
    background: var(--stage);
    font-family: "Open Sans", Arial, sans-serif;
  }
  .stage {
    position: relative; width: 1200px; height: 900px;
    display: flex; flex-direction: column; align-items: center; justify-content: center; gap: 50px;
  }
  .card {
    position: relative; width: 560px; height: 320px;
    border-radius: 18px; overflow: hidden;
  }
  .card--back {
    background: var(--card-black);
    display: flex; align-items: center; justify-content: center;
  }
  .brand-name {
    font-family: "Open Sans", Arial, sans-serif;
    font-weight: 600; text-align: center; line-height: 1.25;
  }
  .card--back .brand-name { color: var(--mark-light); font-size: 26px; }
  .brand-name small { display: block; font-size: 0.55em; letter-spacing: 2px; }
  .card--front { background: var(--card-white); }
  .front-brand {
    position: absolute; left: 30px; top: 95px; width: 190px;
    color: var(--ink); font-size: 24px;
  }
  .divider {
    position: absolute; left: 240px; top: 40px; width: 1px; height: 190px;
    background: var(--rule);
  }
  .details { position: absolute; left: 262px; top: 48px; color: var(--ink); }
  .person-name {
    font-family: "Libre Baskerville", Georgia, serif;
    font-size: 20px; font-weight: 400;
  }
  .person-title {
    font-family: "Libre Baskerville", Georgia, serif;
    font-size: 13px; color: var(--ink-soft); margin-bottom: 12px;
  }
  .address { font-size: 12px; margin-bottom: 8px; }
  .contact-list { list-style: none; font-size: 13px; line-height: 1.45; }
  .contact-list li { display: flex; align-items: center; gap: 8px; }
  .contact-list li.indent { padding-left: 22px; }
  .contact-list svg { width: 14px; height: 14px; fill: var(--ink); flex: none; }
  .band-grey { position: absolute; left: 0; right: 0; bottom: 34px; height: 12px; background: var(--band-grey); }
  .band-black { position: absolute; left: 0; right: 0; bottom: 0; height: 34px; background: var(--band-black); }
</style>
</head>
<body>
<main class="stage">
  <section class="card card--back" aria-label="Card back">
    <p class="brand-name">K&amp;R<small>SECURITY SERVICES</small></p>
  </section>

  <section class="card card--front" aria-label="Card front">
    <p class="brand-name front-brand">K&amp;R<small>SECURITY SERVICES PTY. LTD.</small></p>
    <div class="divider"></div>
    <div class="details">
      <h1 class="person-name">Your name Here</h1>
      <p class="person-title">Title Here</p>
      <p class="address">P.O. Box 12 Lorimer Victoria 3000</p>
      <ul class="contact-list">
        <li>
          <svg viewBox="0 0 16 16" aria-hidden="true"><path d="M2 5c0-2 2-3 12-3 0 0 0 3-3 3l-1-1H6L5 5C2 5 2 5 2 5zM3 7h10l1 7H2z"/></svg>
          (03) 5550 1847
        </li>
        <li>
          <svg viewBox="0 0 16 16" aria-hidden="true"><path d="M5 1h6a1 1 0 0 1 1 1v12a1 1 0 0 1-1 1H5a1 1 0 0 1-1-1V2a1 1 0 0 1 1-1zm0 2v9h6V3z"/></svg>
          0400 555 218
        </li>
        <li>
          <svg viewBox="0 0 16 16" aria-hidden="true"><path d="M1 3h14v10H1zm1.5 1.5v.4L8 8.6l5.5-3.7v-.4zM2.5 6.7v4.8h11V6.7L8 10.4z"/></svg>
          owen@krguardline.net.au
        </li>
        <li class="indent">K.R@krguardline.net.au</li>
      </ul>
    </div>
    <div class="band-grey"></div>
    <div class="band-black"></div>
  </section>
</main>
</body>
</html>
```